Silken Roam (A luxury Travel Website)

website text attached in document below

images also attached

feel free to use other images if needed

Target Market(s)

Luxury Seekers and wealthy couples / families

Industry/Entity Type

Luxury Travel

Coding

Coded - Design and coding required

Number of Pages Required

1 page

Requirements
Must have
• A luxury design and easy use.
Nice to have
• Ease of use of page, incorporation of images into the flow of the site

```html
<!DOCTYPE html>
<html lang="en">
<head>
<meta charset="utf-8">
<title>Silken Roam</title>
<link href="https://fonts.googleapis.com/css2?family=Poppins:wght@400;500;600&display=swap" rel="stylesheet">
<style>
:root{
  --brand:#1e73c8;
  --brand-deep:#1463b0;
  --brand-soft:#5aa3e0;
  --ink:#222;
  --logo:#6f9fc8;
  --white:#fff;
  --muted:#666;
}
*{box-sizing:border-box;margin:0;padding:0}
html,body{width:745px;height:1200px;overflow:hidden;background:var(--white)}
body{font-family:'Poppins',sans-serif;position:relative}
.page{position:relative;width:745px;height:1200px}

.site-header{position:absolute;top:0;left:0;width:745px;height:52px;display:flex;align-items:center;justify-content:center}
.brand-name{font-family:'Poppins',sans-serif;font-weight:400;color:var(--logo);letter-spacing:2px;text-transform:uppercase;font-size:18px}

.hero{position:absolute;top:52px;left:0;width:745px;height:375px;overflow:hidden;
  background:linear-gradient(180deg,#9cbfe6 0%,#5b86b8 28%,#2e5274 55%,#3b5d78 70%,#1d5fa8 85%,#163f6e 100%)}
.hero-photo{position:absolute;inset:0}
.hero-glow{position:absolute;left:500px;top:230px;width:230px;height:90px;border-radius:50%;
  background:radial-gradient(closest-side,rgba(255,190,110,.55),rgba(255,190,110,0))}
.hero-ring{position:absolute;left:233px;top:33px;width:282px;height:282px;border-radius:50%;background:rgba(60,140,220,.35)}
.hero-circle{position:absolute;left:240px;top:42px;width:270px;height:270px;border-radius:50%;background:rgba(30,118,208,.88);
  text-align:center;color:var(--white)}
.hero-title{position:absolute;left:0;right:0;top:62px;font-weight:600;font-size:18px;line-height:24.5px}
.hero-text{position:absolute;left:0;right:0;top:142px;font-weight:500;font-size:10.4px;line-height:17.5px}
.btn{display:block;width:112px;height:30px;border:1.5px solid var(--white);border-radius:16px;color:var(--white);
  font-weight:500;font-size:12px;line-height:27px;text-align:center;text-transform:uppercase;text-decoration:none;background:transparent}
.hero .btn{position:absolute;left:317px;top:231px}
.torn{position:absolute;left:0;width:745px;display:block}

.promise{position:absolute;top:456px;left:0;width:745px;text-align:center}
.section-title{font-weight:600;font-size:16px;line-height:25.5px;text-transform:uppercase;color:var(--ink)}
.rule{width:81px;height:2px;margin:10px auto 0;background:var(--brand)}
.feature{position:absolute;top:540px;width:246px;height:225px}
.feature-hotel{left:103px}
.feature-flight{left:399px}

.enquiry{position:absolute;top:808px;left:0;width:745px;height:336px;background:linear-gradient(160deg,#1b6cbf,#1260ae 60%,#1769bb)}
.enquiry-title{position:absolute;top:47px;left:0;width:745px;text-align:center;color:var(--white)}
.enquiry-title .section-title{color:var(--white)}
.enquiry-title .rule{background:var(--white);margin-top:8px}
.field{position:absolute;background:var(--white);border:none;border-radius:2px;color:var(--brand-deep);
  font-family:'Poppins',sans-serif;font-weight:500;font-size:8.2px;padding:0 11px;display:flex;align-items:center}
.field.area{align-items:flex-start;padding-top:12px}
.enquiry .btn{position:absolute;left:317px;top:260px}

.site-footer{position:absolute;top:1150px;left:0;width:745px;height:50px}
.site-footer .brand-name{position:absolute;left:85px;top:12px}
.copyright{position:absolute;right:82px;top:18px;font-size:8px;color:var(--muted);text-transform:uppercase}
</style>
</head>
<body>
<div class="page">
  <header class="site-header">
    <span class="brand-name">Silken Roam</span>
  </header>

  <section class="hero">
    <div class="hero-photo" role="img" aria-label="Luxury resort with palm trees and an infinity pool at dusk"></div>
    <div class="hero-glow"></div>
    <div class="hero-ring"></div>
    <div class="hero-circle">
      <h1 class="hero-title">Looking to stay at<br>a 5 star hotel or to fly<br>business class anywhere?</h1>
      <p class="hero-text">Share a screenshot of your travel plans and<br>we beat the price, within 24 hours.</p>
    </div>
    <a class="btn" href="#enquiry">Book Now</a>
    <svg class="torn" style="bottom:0" width="745" height="40" viewBox="0 0 745 40" aria-hidden="true">
      <path fill="#fff" d="M0 22 L14 20 L30 23 L48 16 L62 19 L80 12 L96 18 L112 14 L130 21 L146 17 L160 25 L178 30 L196 26 L214 20 L232 24 L248 15 L262 11 L278 17 L296 22 L314 27 L330 32 L342 28 L356 22 L372 18 L388 24 L402 13 L418 9 L432 15 L448 20 L464 16 L480 24 L496 30 L510 25 L526 18 L544 22 L560 14 L576 10 L592 17 L608 24 L624 28 L640 22 L656 17 L672 12 L688 18 L704 21 L720 16 L736 19 L745 17 L745 40 L0 40 Z"/>
    </svg>
  </section>

  <section class="promise">
    <h2 class="section-title">We work directly with hotels and<br>airlines to get you the best price,always</h2>
    <div class="rule"></div>
  </section>

  <svg class="feature feature-hotel" viewBox="0 0 246 225" role="img" aria-label="Luxury hotel bedroom with a large white bed">
    <defs><linearGradient id="hotelTone" x1="0" y1="0" x2="0" y2="1">
      <stop offset="0" stop-color="#c9c4c6"/><stop offset=".25" stop-color="#7f9583"/><stop offset=".6" stop-color="#a8b2aa"/><stop offset=".8" stop-color="#eceef4"/><stop offset="1" stop-color="#f6f6fa"/></linearGradient></defs>
    <path fill="var(--brand-soft)" d="M20 60 C40 45 80 52 110 60 C150 70 190 50 220 70 C245 90 244 150 215 175 C185 200 120 210 70 190 C30 175 0 150 8 110 C12 85 10 70 20 60 Z"/>
    <path fill="url(#hotelTone)" d="M130 0 C160 -2 185 20 188 55 C192 90 240 110 245 150 C248 190 200 212 160 220 C120 228 80 210 60 175 C45 150 10 160 0 125 C-3 100 15 85 40 80 C75 74 85 45 100 20 C107 8 118 1 130 0 Z"/>
  </svg>

  <svg class="feature feature-flight" viewBox="0 0 246 225" role="img" aria-label="Traveller relaxing in a business class airline seat">
    <defs><linearGradient id="flightTone" x1="0" y1="0" x2="1" y2="1">
      <stop offset="0" stop-color="#d6b99d"/><stop offset=".35" stop-color="#b89780"/><stop offset=".7" stop-color="#5a4038"/><stop offset="1" stop-color="#2d1f1c"/></linearGradient></defs>
    <path fill="var(--brand-soft)" d="M25 60 C55 45 95 55 130 58 C170 62 210 45 235 70 C250 95 240 140 215 168 C190 195 140 200 100 190 C55 180 10 160 6 115 C4 90 10 70 25 60 Z"/>
    <path fill="url(#flightTone)" d="M115 0 C150 -3 168 25 180 45 C195 70 238 78 246 120 C252 160 215 178 185 185 C150 195 120 228 80 224 C40 220 0 195 2 150 C4 115 20 105 40 95 C70 82 58 40 80 16 C90 6 102 1 115 0 Z"/>
  </svg>

  <section class="enquiry" id="enquiry">
    <div role="img" aria-label="Faint aerial view of an island resort" style="position:absolute;inset:0;background:radial-gradient(ellipse at 30% 40%,rgba(255,255,255,.05),rgba(255,255,255,0) 60%)"></div>
    <svg class="torn" style="top:0" width="745" height="30" viewBox="0 0 745 30" aria-hidden="true">
      <path fill="#fff" d="M0 0 L745 0 L745 12 L728 14 L712 10 L694 16 L676 12 L660 20 L648 28 L636 18 L618 14 L600 18 L584 12 L566 15 L548 10 L530 16 L512 13 L494 17 L476 12 L458 16 L440 24 L428 28 L416 20 L398 16 L380 12 L364 18 L352 28 L340 22 L322 16 L304 12 L286 16 L268 14 L250 20 L236 16 L220 14 L200 18 L180 14 L160 26 L148 18 L130 12 L112 16 L96 12 L80 16 L62 14 L44 18 L26 13 L10 14 L0 12 Z"/>
    </svg>
    <div class="enquiry-title">
      <h2 class="section-title">Tell us about your next holiday plans</h2>
      <div class="rule"></div>
    </div>
    <div class="field" style="left:176px;top:96px;width:191px;height:29px">First Name*</div>
    <div class="field" style="left:378px;top:96px;width:191px;height:29px">Last Name*</div>
    <div class="field" style="left:176px;top:133px;width:191px;height:29px">Email address*</div>
    <div class="field" style="left:378px;top:133px;width:191px;height:29px">Phone*</div>
    <div class="field area" style="left:176px;top:170px;width:393px;height:76px">Your message</div>
    <a class="btn" href="#enquiry">Book Now</a>
    <svg class="torn" style="bottom:0" width="745" height="34" viewBox="0 0 745 34" aria-hidden="true">
      <path fill="#fff" d="M0 28 L16 26 L34 20 L52 24 L70 18 L88 22 L104 14 L120 8 L136 14 L150 20 L166 12 L182 16 L198 22 L214 14 L232 18 L250 24 L266 30 L280 22 L296 14 L312 10 L328 16 L344 24 L360 20 L376 26 L392 18 L410 12 L426 22 L442 30 L458 24 L474 16 L490 12 L506 18 L520 14 L536 8 L552 14 L568 20 L584 16 L600 22 L616 18 L632 12 L648 16 L664 22 L680 18 L698 24 L716 20 L732 24 L745 22 L745 34 L0 34 Z"/>
    </svg>
  </section>

  <footer class="site-footer">
    <span class="brand-name">Silken Roam</span>
    <p class="copyright">© 2022 Silken Roam all right reserved</p>
  </footer>
</div>
</body>
</html>
```